Doctors clinic requires stationary designed

We require various types of stationary to be design based on the logo (attached). We require the following:
- Letterhead (A4 Portrait)
- Business Card (must include UV spot on rear)
- With compliments slip (DL Landscape)
- Appointments card (Folded A6)

We are a young clinical practice which boasts a modern and sophisticated approach to medicine so we require something which feels fresh and modern. Please include colours represented in the logo (contrasting teal and grey). We are calling for creative minds to put forth their ideas and we will be actively providing feedback on all designs.

thank you

Clinic

```html
<!DOCTYPE html>
<html lang="en">
<head>
<meta charset="utf-8">
<title>Dr Clara Whitfield – Stationery Set</title>
<link href="https://fonts.googleapis.com/css2?family=Open+Sans:wght@400;600&display=swap" rel="stylesheet">
<style>
  :root{
    --teal:#16988d;
    --teal-dark:#0f8479;
    --mint:#86c8a4;
    --grey:#6b6f72;
    --grey-light:#9a9ea1;
    --paper:#f7f7f7;
    --stage:#e4e6e6;
    --ring:#bfe0db;
  }
  *{box-sizing:border-box;margin:0;padding:0}
  html,body{width:1048px;height:1200px;overflow:hidden}
  body{background:var(--stage);font-family:"Open Sans",Arial,sans-serif;color:var(--grey);position:relative}
  .sheet{position:absolute;background:var(--paper);overflow:hidden;box-shadow:0 2px 6px rgba(0,0,0,.12)}
  .brand{position:absolute;display:flex;align-items:center;gap:8px}
  .brand-dot{border:2px solid var(--teal);border-radius:50%;flex:none}
  .brand-name{color:var(--teal);font-weight:600;white-space:nowrap;line-height:1}
  .brand-role{position:absolute;color:var(--grey);white-space:nowrap}
  .bands{position:absolute;left:0;bottom:0;width:100%;display:block}
  .deco-ring{position:absolute;border:2px solid var(--ring);border-radius:50%}

  /* Letterhead */
  .letterhead{left:40px;top:40px;width:488px;height:690px}
  .letterhead .brand{left:128px;top:34px}
  .letterhead .brand-dot{width:30px;height:30px}
  .letterhead .brand-name{font-size:17px}
  .letterhead .brand-role{left:166px;top:58px;font-size:9px}
  .letter-title{position:absolute;left:140px;top:146px;font-size:14px;font-weight:600;color:#3d4245}
  .letter-meta{position:absolute;left:20px;top:178px;width:104px;text-align:right;font-size:6.5px;line-height:9px}
  .letter-meta dt{color:var(--teal);font-size:8px;font-weight:600}
  .letter-meta dd{margin-bottom:10px}
  .letter-body{position:absolute;left:140px;top:182px;width:305px;font-size:6.6px;line-height:9.2px;color:#50555a}
  .letter-body p{margin-bottom:9px}
  .signoff{position:absolute;left:140px;top:556px;font-size:8px;color:#3d4245}
  .signoff small{display:block;font-size:6px;color:var(--grey-light)}
  .letterhead .deco-ring{left:330px;top:548px;width:78px;height:78px}

  /* Business cards */
  .card{left:584px;width:420px;height:256px}
  .card-front{top:96px;background:linear-gradient(120deg,var(--teal) 0%,var(--mint) 100%);display:flex;align-items:center;justify-content:center;gap:14px}
  .card-front .brand-dot{width:46px;height:46px;border-color:#fff}
  .card-front .brand-name{color:#fff;font-size:24px}
  .card-back{top:392px}
  .card-back .brand{left:26px;top:34px}
  .card-back .brand-dot{width:30px;height:30px}
  .card-back .brand-name{font-size:17px}
  .card-back .brand-role{left:64px;top:58px;font-size:9px}
  .card-contact{position:absolute;font-size:8px;line-height:12px;color:var(--grey)}
  .card-contact.right{left:250px;top:108px}
  .card-contact.left{left:26px;top:168px}
  .card-back .deco-ring{left:330px;top:150px;width:90px;height:90px}

  /* Envelopes */
  .envelope{top:786px;width:474px;height:260px;background:#f1f2f2}
  .env-front{left:40px}
  .env-front .brand{left:120px;top:30px}
  .env-front .brand-dot{width:34px;height:34px}
  .env-front .brand-name{font-size:19px}
  .env-front .brand-role{left:162px;top:58px;font-size:10px}
  .env-window{position:absolute;left:234px;top:150px;width:200px;height:80px;background:#fff;border:1px solid #dcdede;border-radius:10px}
  .env-contact{position:absolute;font-size:9px;line-height:12px;color:var(--grey)}
  .env-front .env-contact.top{left:14px;top:168px}
  .env-front .env-contact.bottom{left:14px;top:208px}
  .env-back{left:534px}
  .env-back .deco-ring{left:20px;top:130px;width:110px;height:110px}
  .env-back .env-contact{right:16px;top:212px;text-align:right}
  .flap{position:absolute;left:0;top:0;width:100%;display:block}
</style>
</head>
<body>

<section class="sheet letterhead" aria-label="Letterhead">
  <div class="brand"><span class="brand-dot"></span><span class="brand-name">Dr Clara Whitfield</span></div>
  <div class="brand-role">Obstetrician and Gynaecologist</div>

  <h1 class="letter-title">Lorem ipsum dolor sit amet</h1>

  <dl class="letter-meta">
    <dt>Date:</dt><dd>01-02-2017</dd>
    <dt>Address:</dt>
    <dd>14 Harbour Row<br>Leeds<br>LS1 4QT<br>Ph: +44 113 496 0021<br>+44 113 496 0188</dd>
  </dl>

  <div class="letter-body">
    <p>Lorem Ipsum is simply dummy text of the printing and typesetting industry. Lorem Ipsum has been the industry's standard dummy text ever since the 1500s, when an unknown printer took a galley of type and scrambled it to make a type specimen book. It has survived not only five centuries, but also the leap into electronic typesetting, remaining essentially unchanged. It was popularised in the 1960s with the release of Letraset sheets containing Lorem Ipsum passages, and more recently with desktop publishing software like Aldus PageMaker including versions of Lorem Ipsum.</p>
    <p>It is a long established fact that a reader will be distracted by the readable content of a page when looking at its layout. The point of using Lorem Ipsum is that it has a more-or-less normal distribution of letters, as opposed to using 'Content here, content here', making it look like readable English. Many desktop publishing packages and web page editors now use Lorem Ipsum as their default model text, and a search for 'lorem ipsum' will uncover many web sites still in their infancy. Various versions have evolved over the years, sometimes by accident, sometimes on purpose (injected humour and the like).</p>
    <p>obscure Latin words, consectetur, from a Lorem Ipsum passage, and going through the cites of the word in classical literature, discovered the undoubtable source. Lorem Ipsum comes from sections 1.10.32</p>
  </div>

  <div class="signoff">Ian Harlow<small>Date: 01-02-2018</small></div>
  <div class="deco-ring"></div>

  <svg class="bands" viewBox="0 0 488 64" height="64" preserveAspectRatio="none" aria-hidden="true">
    <polygon points="0,8 488,26 488,64 0,64" fill="var(--mint)"/>
    <polygon points="0,30 488,12 488,64 0,64" fill="var(--teal)"/>
  </svg>
</section>

<section class="sheet card card-front" aria-label="Business card front">
  <span class="brand-dot"></span><span class="brand-name">Dr Clara Whitfield</span>
</section>

<section class="sheet card card-back" aria-label="Business card back">
  <div class="brand"><span class="brand-dot"></span><span class="brand-name">Dr Clara Whitfield</span></div>
  <div class="brand-role">Obstetrician and Gynaecologist</div>
  <div class="card-contact right">T: 0113 496 0021<br>M: 07700 900 481<br>info@harbourclinic.co.uk</div>
  <div class="card-contact left">14 Harbour Row, Leeds<br>LS1 4QT</div>
  <div class="deco-ring"></div>
  <svg class="bands" viewBox="0 0 420 30" height="30" preserveAspectRatio="none" aria-hidden="true">
    <polygon points="0,6 420,14 420,30 0,30" fill="var(--mint)"/>
    <polygon points="0,18 420,6 420,30 0,30" fill="var(--teal)"/>
  </svg>
</section>

<section class="sheet envelope env-front" aria-label="Envelope front">
  <div class="brand"><span class="brand-dot"></span><span class="brand-name">Dr Clara Whitfield</span></div>
  <div class="brand-role">Obstetrician and Gynaecologist</div>
  <div class="env-contact top">info@harbourclinic.co.uk<br>www.harbourclinic.co.uk</div>
  <div class="env-contact bottom">Tel-01134960021<br>Fax-01134960022<br>Mobile-07700900481</div>
  <div class="env-window"></div>
</section>

<section class="sheet envelope env-back" aria-label="Envelope back">
  <svg class="flap" viewBox="0 0 474 40" height="40" preserveAspectRatio="none" aria-hidden="true">
    <polygon points="0,0 474,0 474,22 0,40" fill="var(--teal)"/>
    <polygon points="0,0 474,0 474,8 0,26" fill="var(--mint)"/>
  </svg>
  <div class="deco-ring"></div>
  <div class="env-contact">info@harbourclinic.co.uk<br>www.harbourclinic.co.uk</div>
</section>

</body>
</html>
```